Banner poster with different motifs

I'm looking for 5 banners and posters in A1 format in the same design, or the similarity must be recognizable...
Kept quite simple with different titles.

1 ballet
2 Contemporary Dance
3 high heels
4 Salsa & Bachata & Zouk
5 Hip Hop

Modern bright colors
it is for the entrance so that the students see here is a dance school

The text may also be included in the image
The photos are for guidance only; some are our own, some are purchased. However, we are permitted to use them, including our logo, of course.

```html
<!DOCTYPE html>
<html lang="en">
<head>
<meta charset="utf-8">
<title>Solvista Dance Center – Class Banners</title>
<link href="https://fonts.googleapis.com/css2?family=Bebas+Neue&display=swap" rel="stylesheet">
<style>
  :root {
    --sheet: #ffffff;
    --black: #0a0508;
    --deep: #3a0722;
    --plum: #7a0f47;
    --magenta: #c5127a;
    --pink: #e0178a;
    --rose: #d42e8c;
    --white: #ffffff;
    --photo-skin: #b86a7e;
    --photo-dark: #2a1420;
  }
  * { box-sizing: border-box; margin: 0; padding: 0; }
  html, body { width: 934px; height: 1200px; overflow: hidden; background: var(--sheet); }
  body { font-family: "Bebas Neue", "Oswald", sans-serif; position: relative; }

  .banner {
    position: absolute;
    left: 52px;
    width: 830px;
    height: 201px;
    overflow: hidden;
  }
  .banner--ballet { top: 53px; background: linear-gradient(20deg, var(--magenta) 0%, var(--plum) 30%, var(--deep) 55%, var(--black) 80%); }
  .banner--contemporary { top: 276px; background: linear-gradient(100deg, var(--black) 0%, var(--black) 28%, var(--deep) 55%, var(--plum) 75%, var(--magenta) 100%); }
  .banner--latin { top: 499px; background: linear-gradient(90deg, var(--magenta) 0%, var(--plum) 30%, var(--deep) 55%, var(--black) 72%); }
  .banner--heels { top: 722px; background: linear-gradient(100deg, var(--rose) 0%, var(--magenta) 45%, #a8154f 100%); }
  .banner--hiphop { top: 945px; background: linear-gradient(180deg, var(--pink) 0%, var(--plum) 40%, var(--deep) 70%, var(--black) 100%); }

  .title {
    position: absolute;
    font-size: 104px;
    line-height: 90px;
    letter-spacing: 1px;
    color: var(--white);
    white-space: nowrap;
    z-index: 2;
  }
  .title .accent { color: var(--pink); }
  .title span { display: block; }

  .banner--ballet .title { left: 29px; top: 22px; }
  .banner--contemporary .title { left: 24px; top: 22px; }
  .banner--latin .title { right: 32px; top: 22px; text-align: right; }
  .banner--heels .title { top: 40px; font-size: 140px; line-height: 130px; }
  .banner--heels .title--left { left: 26px; }
  .banner--heels .title--right { right: 22px; }
  .banner--hiphop .title { left: 26px; top: 48px; font-size: 118px; line-height: 110px; }

  .photo {
    position: absolute;
    top: 0;
    height: 100%;
    z-index: 1;
  }
  .banner--ballet .photo { left: 266px; width: 337px; background: radial-gradient(ellipse at 50% 50%, rgba(40,20,30,0.85) 0%, rgba(184,106,126,0.35) 45%, transparent 70%); }
  .banner--contemporary .photo { left: 478px; width: 352px; background: radial-gradient(ellipse at 60% 55%, rgba(30,25,40,0.8) 0%, rgba(184,106,126,0.35) 45%, transparent 70%); }
  .banner--latin .photo { left: 25px; width: 333px; background: radial-gradient(ellipse at 45% 55%, rgba(184,106,126,0.6) 0%, rgba(60,30,50,0.4) 45%, transparent 72%); }
  .banner--heels .photo { left: 238px; width: 291px; background: radial-gradient(ellipse at 50% 55%, rgba(30,15,25,0.75) 0%, rgba(184,106,126,0.35) 45%, transparent 70%); }
  .banner--hiphop .photo { left: 450px; width: 113px; background: radial-gradient(ellipse at 50% 55%, rgba(20,10,15,0.85) 0%, rgba(184,106,126,0.3) 50%, transparent 75%); }

  .brand {
    position: absolute;
    z-index: 2;
    color: var(--white);
    text-align: center;
    display: flex;
    flex-direction: column;
    align-items: center;
  }
  .brand__dot {
    width: 48px;
    height: 48px;
    border: 1.5px solid var(--white);
    border-radius: 50%;
    margin-bottom: 10px;
  }
  .brand__name { font-size: 34px; line-height: 30px; letter-spacing: 3px; }
  .brand__tagline { font-size: 11px; line-height: 12px; letter-spacing: 2.6px; margin-top: 2px; }

  .banner--ballet .brand { left: 577px; top: 38px; width: 200px; }
  .banner--hiphop .brand { left: 568px; top: 40px; width: 200px; }
  .banner--contemporary .brand { left: 322px; top: 108px; width: 150px; }
  .banner--contemporary .brand__dot { width: 34px; height: 34px; margin-bottom: 6px; }
  .banner--contemporary .brand__name { font-size: 24px; line-height: 22px; letter-spacing: 2px; }
  .banner--contemporary .brand__tagline { font-size: 8px; line-height: 9px; letter-spacing: 1.8px; }
</style>
</head>
<body>

  <section class="banner banner--ballet">
    <h2 class="title"><span class="accent">Ballet</span><span>Dance</span></h2>
    <div class="photo" role="img" aria-label="Photo of a ballet dancer in pointe shoes arching backward in a deep lunge"></div>
    <div class="brand">
      <div class="brand__dot"></div>
      <div class="brand__name">SOLVISTA</div>
      <div class="brand__tagline">DANCE CENTER FRANKFURT</div>
    </div>
  </section>

  <section class="banner banner--contemporary">
    <h2 class="title"><span>Contemporary</span><span class="accent">Dance</span></h2>
    <div class="brand">
      <div class="brand__dot"></div>
      <div class="brand__name">SOLVISTA</div>
      <div class="brand__tagline">DANCE CENTER FRANKFURT</div>
    </div>
    <div class="photo" role="img" aria-label="Photo of a contemporary dancer leaping with one arm raised"></div>
  </section>

  <section class="banner banner--latin">
    <div class="photo" role="img" aria-label="Photos of a salsa couple embracing and a pair of partner dancers in a lift"></div>
    <h2 class="title"><span class="accent">Salsa and</span><span>Bachata &amp; Zouk</span></h2>
  </section>

  <section class="banner banner--heels">
    <h2 class="title title--left">High</h2>
    <div class="photo" role="img" aria-label="Photo of a dancer in black outfit and high heels posing in a squat"></div>
    <h2 class="title title--right">Heels</h2>
  </section>

  <section class="banner banner--hiphop">
    <h2 class="title">Hip Hop</h2>
    <div class="photo" role="img" aria-label="Photo of a hip hop dancer in black clothes in a dynamic pose"></div>
    <div class="brand">
      <div class="brand__dot"></div>
      <div class="brand__name">SOLVISTA</div>
      <div class="brand__tagline">DANCE CENTER FRANKFURT</div>
    </div>
  </section>

</body>
</html>
```